Maple Crest Schools | brand new stationery!

We need stationery design with our new logo! Our company updated it's name and image and we like to incorporate the new one on our stationery, business cards and email signature. We are looking for fresh, new ideas!
Industry: Childcare, Elementary and Middle School
Company Name: Maple Crest Schools
Tagline: Bright Futures Start Here
Main colors: Blue, white and a little yellow
Star shape is something new for us! Do you see a way to incorporate it as a design element?

```html
<!DOCTYPE html>
<html lang="en">
<head>
<meta charset="UTF-8">
<title>Maple Crest Schools – Business Card</title>
<link href="https://fonts.googleapis.com/css2?family=Montserrat:wght@400;500;700;800&display=swap" rel="stylesheet">
<style>
  :root {
    --backdrop: #2b2b2b;
    --card-dark: #231f20;
    --card-light: #ffffff;
    --navy: #262b6b;
    --yellow: #f7c21b;
    --ink: #231f20;
    --ink-soft: #3a3a3a;
    --white: #ffffff;
  }
  * { margin: 0; padding: 0; box-sizing: border-box; }
  html, body {
    width: 1200px; height: 866px; overflow: hidden;
    background: var(--backdrop);
    font-family: "Montserrat", sans-serif;
  }
  .stage { position: relative; width: 1200px; height: 866px; }
  .card {
    position: absolute; left: 250px; width: 700px; height: 400px;
    overflow: hidden;
  }
  .card--back { top: 22px; background: var(--card-dark); }
  .card--front { top: 444px; background: var(--card-light); }

  /* Back */
  .back-brand {
    position: absolute; left: 0; right: 0; top: 84px;
    display: flex; flex-direction: column; align-items: center;
  }
  .brand-dot {
    width: 58px; height: 58px; border-radius: 50%;
    background: var(--navy); margin-bottom: 18px;
  }
  .brand-name {
    font-weight: 700; color: var(--white); text-align: center;
    line-height: 1.02;
  }
  .back-brand .brand-name { font-size: 50px; }
  .brand-name span { display: block; }
  .tagline {
    margin-top: 38px; color: var(--yellow);
    font-size: 29px; font-weight: 500; letter-spacing: 0.5px;
  }

  /* Front */
  .front-mark {
    position: absolute; right: -40px; top: 40px;
    width: 330px; height: 330px; border-radius: 50%;
    background: var(--navy);
  }
  .front-brand {
    position: absolute; left: 48px; top: 40px;
  }
  .front-brand .brand-name { color: var(--ink); font-size: 44px; text-align: left; }
  .person { position: absolute; left: 52px; top: 166px; }
  .person-name {
    color: var(--navy); font-weight: 800; font-size: 27px; line-height: 32px;
    letter-spacing: -0.3px; text-transform: uppercase;
  }
  .person-role { color: var(--ink-soft); font-size: 17px; line-height: 22px; margin-top: 2px; }
  .contacts { list-style: none; margin-top: 12px; }
  .contacts li {
    display: flex; align-items: center; gap: 12px;
    color: var(--ink-soft); font-size: 16px; line-height: 26px;
  }
  .contacts svg { width: 16px; height: 16px; flex: none; }
  .address { margin-top: 10px; color: var(--ink-soft); font-size: 16px; line-height: 22px; }
</style>
</head>
<body>
<main class="stage">
  <section class="card card--back">
    <div class="back-brand">
      <div class="brand-dot"></div>
      <h1 class="brand-name"><span>Maple Crest</span><span>Schools</span></h1>
      <p class="tagline">Bright Futures Start Here</p>
    </div>
  </section>

  <section class="card card--front">
    <div class="front-mark"></div>
    <div class="front-brand">
      <h2 class="brand-name"><span>Maple Crest</span><span>Schools</span></h2>
    </div>
    <div class="person">
      <p class="person-name">Daniel Harper</p>
      <p class="person-role">Managing Director</p>
      <ul class="contacts">
        <li>
          <svg viewBox="0 0 16 16"><path fill="#262b6b" d="M3.5 1.5l2.2 2.6-1.2 1.6c.9 2 2.4 3.5 4.4 4.4l1.6-1.2 2.6 2.2-1.3 2.4C6.6 13.3 2.7 9.4 1.1 4.2z"/></svg>
          031-555 208 614
        </li>
        <li>
          <svg viewBox="0 0 16 16"><rect x="1" y="3" width="14" height="10" fill="#262b6b"/><path d="M1.5 3.5L8 9l6.5-5.5" fill="none" stroke="#fff" stroke-width="1.2"/></svg>
          hello@maplecrestschools.org
        </li>
        <li>
          <svg viewBox="0 0 16 16"><circle cx="8" cy="8" r="7" fill="#262b6b"/><path d="M1 8h14M8 1c-3 3.5-3 10.5 0 14M8 1c3 3.5 3 10.5 0 14" fill="none" stroke="#fff" stroke-width="1"/></svg>
          www.maplecrestschools.org
        </li>
      </ul>
      <p class="address">88, Willow Bend Road<br>Fairhaven, 30718</p>
    </div>
  </section>
</main>
</body>
</html>
```